Business Card Design

I need a Business Card that will catch the attention that will not get thrown in a Drawer. I have 23 companies I use for Auto, Home, Life, and Business Insurance. I make sure that people have the best coverage for the $ spent.

Industry/Entity Type

Business

Contact Information for Business Card

Dorlin Insurance Agency, Inc., Marcus Helgren, 4375 West Tamber Lane Brennick Falls, Nordale 45192 555-281-7496, www.dorlinagency.example, Facebook, LinkedIn, Google+

```html
<!DOCTYPE html>
<html lang="en">
<head>
<meta charset="utf-8">
<title>Dorlin Insurance Agency, Inc. — Business Card</title>
<link rel="stylesheet" href="https://fonts.googleapis.com/css2?family=Open+Sans:wght@400;700&display=swap">
<style>
  :root {
    --ink: #000000;
    --paper: #ffffff;
    --sheen-edge: #bdbdbd;
    --sheen-mid: #f7f7f7;
    --sheen-low: #cfcfcf;
    --figure-dark: #111111;
    --figure-light: #3a3a3a;
  }
  html, body {
    margin: 0;
    padding: 0;
    width: 1200px;
    height: 702px;
    overflow: hidden;
    background: var(--paper);
  }
  .canvas {
    position: relative;
    width: 1200px;
    height: 702px;
    overflow: hidden;
    background: var(--paper);
  }
  .card {
    position: absolute;
    left: 44px;
    top: 44px;
    width: 1109px;
    height: 611px;
    border: 3px solid var(--ink);
    box-sizing: border-box;
    background: linear-gradient(to bottom, var(--sheen-edge) 0%, var(--sheen-mid) 42%, var(--paper) 58%, var(--sheen-low) 100%);
    overflow: hidden;
  }
  .figure-art {
    position: absolute;
    left: 0;
    top: 0;
  }
  .rule-bands {
    position: absolute;
    left: 0;
    top: 546px;
    width: 1109px;
    height: 24px;
  }
  .brand {
    position: absolute;
    left: 425px;
    margin: 0;
    font-family: "Open Sans", "Helvetica", sans-serif;
    font-weight: 700;
    color: var(--ink);
    line-height: 1;
    white-space: nowrap;
  }
  .brand-first {
    top: 178px;
    font-size: 84px;
    letter-spacing: 2px;
  }
  .brand-second {
    top: 284px;
    font-size: 44px;
  }
  .contact {
    position: absolute;
    left: 425px;
    margin: 0;
    font-family: "Open Sans", "Helvetica", sans-serif;
    font-weight: 400;
    color: var(--ink);
    line-height: 1;
    white-space: nowrap;
  }
  .contact-phone { top: 356px; font-size: 42px; }
  .contact-web { top: 404px; font-size: 42px; }
  .address {
    position: absolute;
    left: 425px;
    top: 470px;
    margin: 0;
    font-family: "Open Sans", "Helvetica", sans-serif;
    font-size: 24px;
    line-height: 32px;
    color: var(--ink);
    font-style: normal;
    white-space: nowrap;
  }
</style>
</head>
<body>
<div class="canvas">
  <div class="card">
    <svg class="figure-art" width="410" height="611" viewBox="0 0 410 611" role="img" aria-label="Striped black and white profile silhouette illustration">
      <defs>
        <linearGradient id="figureTone" x1="0" y1="0" x2="1" y2="0">
          <stop offset="0" stop-color="#111111"/>
          <stop offset="0.5" stop-color="#3a3a3a"/>
          <stop offset="1" stop-color="#111111"/>
        </linearGradient>
      </defs>
      <rect x="86" y="0" width="322" height="611" fill="url(#figureTone)"/>
    </svg>

    <svg class="rule-bands" width="1109" height="24" viewBox="0 0 1109 24" aria-hidden="true">
      <rect x="0" y="0" width="1109" height="5" fill="#000000"/>
      <rect x="0" y="5" width="1109" height="8" fill="#f7f7f7"/>
      <rect x="0" y="13" width="1109" height="3" fill="#000000"/>
    </svg>

    <h1 class="brand brand-first">DORLIN</h1>
    <p class="brand brand-second">INSURANCE AGENCY, INC.</p>

    <p class="contact contact-phone">555-281-7496</p>
    <p class="contact contact-web">www.dorlinagency.example</p>

    <address class="address">
      4375 West Tamber Lane, Brennick Falls,<br>
      Nordale 45192
    </address>
  </div>
</div>
</body>
</html>
```